Business Cards For Glintwell
Desmond Kuvetti
Simple
CEO and Founder
2871 Pellfield Ln Brockville Ontario K3P2c8
Desmond@Kuvetti-mail.test
Keep it simple and clean. We want the logo BIG on the one side and company info on the other. If you can get some type of interlock going from bad to restored too that might look nice faded as a background on one of the sides.
750PineRidgeRnR 750PineRidgeRnR
https://www.socialpage.test/750PineRidgeRR/photos/pb.382915067214433.-1109384000.1285719304./517293048116520/?type=3&theater this is a good picture that would be nice to have one one side of the cards faded out
Logo has been uploaded.
Grafto Grafto
kindly upload logo

```html
<!DOCTYPE html>
<html lang="en">
<head>
<meta charset="utf-8">
<title>Glintwell Business Cards</title>
<link href="https://fonts.googleapis.com/css2?family=Montserrat:wght@400;500;800&display=swap" rel="stylesheet">
<style>
  :root {
    --backdrop: #1b1b1d;
    --card-light: #fbfbfb;
    --card-shade: #d9d9da;
    --navy: #262f6b;
    --navy-deep: #1c2358;
    --swoosh-grey: #4a4a4d;
    --text-dark: #3a3a3c;
    --white: #ffffff;
  }
  * { box-sizing: border-box; margin: 0; padding: 0; }
  html, body {
    width: 1200px; height: 1042px; overflow: hidden;
    background: var(--backdrop);
    font-family: "Montserrat", Arial, sans-serif;
  }
  .canvas { position: relative; width: 1200px; height: 1042px; }
  .card {
    position: absolute;
    border-radius: 30px;
    overflow: hidden;
    background: linear-gradient(135deg, var(--card-light) 0%, #f1f1f2 55%, var(--card-shade) 100%);
    box-shadow: 0 14px 30px rgba(0,0,0,0.55);
  }
  .card--front { left: 76px; top: 79px; width: 741px; height: 436px; }
  .card--back  { left: 397px; top: 541px; width: 693px; height: 416px; }

  .header-waves { position: absolute; inset: 0; width: 100%; height: 100%; }

  .holder { position: absolute; left: 24px; top: 24px; color: var(--white); }
  .holder__name { font-size: 28px; font-weight: 500; letter-spacing: 0.5px; line-height: 1.1; }
  .holder__role { font-size: 20px; font-weight: 400; margin-top: 6px; margin-left: 110px; }

  .contact { position: absolute; left: 20px; top: 302px; list-style: none; color: var(--text-dark); font-size: 12px; line-height: 15px; }
  .contact__row { display: flex; align-items: center; gap: 8px; height: 15px; }
  .contact__icon { width: 11px; height: 11px; flex: none; }
  .contact__address { margin-bottom: 4px; line-height: 15px; }

  .wordmark {
    position: absolute;
    color: var(--navy);
    font-weight: 800;
    letter-spacing: 0.5px;
    line-height: 1;
    white-space: nowrap;
  }
  .card--front .wordmark { left: 369px; top: 280px; font-size: 44px; }
  .card--back .wordmark { left: 0; right: 0; top: 185px; text-align: center; font-size: 44px; padding-left: 38px; }
</style>
</head>
<body>
<main class="canvas">
  <section class="card card--front" aria-label="Business card front">
    <svg class="header-waves" viewBox="0 0 672 437" preserveAspectRatio="none" aria-hidden="true">
      <path d="M0 0 H672 V40 C560 60 470 80 380 105 C280 132 160 140 0 150 Z" fill="var(--navy)"/>
      <path d="M0 150 C160 140 280 132 380 105 C470 80 560 60 672 40 V52 C570 72 480 92 400 118 C290 150 160 162 0 165 Z" fill="var(--white)"/>
      <path d="M0 172 C170 168 300 150 410 122 C500 98 590 74 672 58 V66 C590 84 510 108 430 132 C310 166 170 182 0 186 Z" fill="var(--swoosh-grey)"/>
      <path d="M672 96 C600 102 540 130 450 170 L470 170 C550 138 610 116 672 110 Z" fill="var(--navy-deep)"/>
    </svg>
    <div class="holder">
      <p class="holder__name">Corin Adley-Vance</p>
      <p class="holder__role">consultant</p>
    </div>
    <ul class="contact">
      <li class="contact__address">417 Harlow Court<br>Fenwick Road QTR</li>
      <li class="contact__row">
        <svg class="contact__icon" viewBox="0 0 16 16" aria-hidden="true"><path d="M3 2h3l1 3-2 1c1 2 2 3 4 4l1-2 3 1v3c0 1-1 2-2 2C6 14 2 10 2 4c0-1 0-2 1-2z" fill="var(--text-dark)"/></svg>
        012 345 6789</li>
      <li class="contact__row">
        <svg class="contact__icon" viewBox="0 0 16 16" aria-hidden="true"><rect x="4" y="1" width="8" height="14" rx="1.5" fill="var(--text-dark)"/><rect x="5.5" y="3" width="5" height="8" fill="var(--white)"/></svg>
        012 345 6789</li>
      <li class="contact__row">
        <svg class="contact__icon" viewBox="0 0 16 16" aria-hidden="true"><rect x="2" y="4" width="12" height="9" rx="1" fill="var(--text-dark)"/><rect x="4" y="2" width="8" height="4" fill="var(--text-dark)"/><rect x="4" y="9" width="8" height="5" fill="var(--white)"/></svg>
        012 345 6789</li>
      <li class="contact__row">
        <svg class="contact__icon" viewBox="0 0 16 16" aria-hidden="true"><rect x="1" y="3" width="14" height="10" rx="1" fill="var(--text-dark)"/><path d="M1.5 3.5 8 9l6.5-5.5" stroke="var(--white)" stroke-width="1.2" fill="none"/></svg>
        urname@mail.test</li>
      <li class="contact__row">
        <svg class="contact__icon" viewBox="0 0 16 16" aria-hidden="true"><circle cx="8" cy="8" r="6.5" fill="none" stroke="var(--text-dark)" stroke-width="1.4"/><ellipse cx="8" cy="8" rx="2.8" ry="6.5" fill="none" stroke="var(--text-dark)" stroke-width="1.2"/><path d="M1.5 8h13" stroke="var(--text-dark)" stroke-width="1.2"/></svg>
        www.yourwebsite.test</li>
    </ul>
    <p class="wordmark">GLINTWELL</p>
  </section>

  <section class="card card--back" aria-label="Business card back">
    <p class="wordmark">GLINTWELL</p>
  </section>
</main>
</body>
</html>
```